Business Card for Toffee Parlour

I have a logo for my candy buffet business, and need a business card designed using that logo. Toffee Parlour designs and builds beautiful and delicious candy and dessert tables for all kinds of events. The card should be simple, modern, graphic, colorful, and use the Toffee Parlour Logo.

Target Market(s)

The target market is people hosting major parties and events. This includes brides getting married, parents hosting birthday parties/Sweet Sixteen/Bar Mitzvah/quinceanera parties, and companies hosting corporate events.

Industry/Entity Type

Business

Requirements
Must have
• The business card must have the logo, with or without the tag line.

The following information must be on the card:

Renata Hollis
CEO & Candy Stylist
415.372.6091
renata@toffeeparlourco.example
Nice to have
• I like the idea of having multiple colors of the same design so that several people receiving cards will each receive a different color. Perhaps 3-5 colors or variations on a basic card design.

```html
<!DOCTYPE html>
<html lang="en">
<head>
<meta charset="utf-8">
<title>Toffee Parlour Business Card</title>
<link rel="stylesheet" href="https://fonts.googleapis.com/css2?family=Lato:wght@400;700&display=swap">
<style>
  :root {
    --bg: #e9e7e4;
    --card: #ffffff;
    --ink: #222222;
    --blue: #1f73a8;
    --magenta: #a51e6e;
    --orange: #ef8d25;
    --green: #1e8a3e;
    --purple: #4b2c7e;
    --black: #141414;
    --rule: #555555;
  }
  * { box-sizing: border-box; margin: 0; padding: 0; }
  html, body { width: 1200px; height: 1000px; overflow: hidden; }
  body {
    background: var(--bg);
    font-family: "Lato", Arial, sans-serif;
    color: var(--ink);
    position: relative;
  }
  .card {
    position: absolute;
    left: 250px;
    width: 700px;
    height: 400px;
    background: var(--card);
    box-shadow: 0 6px 18px rgba(0,0,0,0.18);
    overflow: hidden;
  }
  .card--back { top: 70px; }
  .card--front { top: 530px; }

  .color-strip {
    position: absolute;
    left: 0; right: 0; bottom: 0;
    height: 48px;
    display: flex;
  }
  .color-strip span { flex: 1; }
  .color-strip .blue { background: var(--blue); }
  .color-strip .magenta { background: var(--magenta); }
  .color-strip .orange { background: var(--orange); }
  .color-strip .green { background: var(--green); }
  .color-strip .purple { background: var(--purple); }
  .color-strip .black { background: var(--black); flex: 0.7; }

  .brand {
    display: flex;
    align-items: center;
    gap: 14px;
    color: var(--ink);
    font-weight: 400;
    white-space: nowrap;
  }
  .brand__dot {
    border-radius: 50%;
    background: var(--magenta);
    flex: none;
  }
  .brand-rule { height: 2px; background: var(--rule); }

  .card--back .brand-lockup {
    position: absolute;
    left: 50%; top: 128px;
    transform: translateX(-50%);
    display: flex; flex-direction: column; align-items: center; gap: 14px;
  }
  .card--back .brand { font-size: 58px; letter-spacing: -0.5px; }
  .card--back .brand__dot { width: 40px; height: 40px; }
  .card--back .brand-rule { width: 440px; }

  .card--front .brand-lockup {
    position: absolute;
    left: 40px; top: 44px;
    display: flex; flex-direction: column; gap: 10px;
  }
  .card--front .brand { font-size: 33px; gap: 10px; }
  .card--front .brand__dot { width: 24px; height: 24px; }
  .card--front .brand-rule { width: 270px; }

  .name-band {
    position: absolute;
    left: 0; top: 140px;
    width: 320px; height: 74px;
    background: var(--blue);
    clip-path: polygon(0 0, 100% 0, 92% 100%, 0 100%);
    display: flex; align-items: center;
    padding-left: 44px;
    color: #fff;
    font-weight: 700;
    font-size: 24px;
    letter-spacing: 0.5px;
    text-transform: uppercase;
  }
  .title-band {
    position: absolute;
    left: 318px; top: 82px;
    right: 0; height: 54px;
    background: var(--magenta);
    clip-path: polygon(3% 0, 100% 0, 100% 100%, 0 100%);
    display: flex; align-items: center;
    padding-left: 44px;
    color: #fff;
    font-weight: 700;
    font-size: 24px;
  }
  .contact-list {
    position: absolute;
    left: 380px; top: 172px;
    list-style: none;
    display: flex; flex-direction: column; gap: 12px;
  }
  .contact-list li {
    display: flex; align-items: center; gap: 16px;
    font-size: 19px;
    color: var(--ink);
  }
  .contact-list svg { width: 18px; height: 18px; flex: none; }
</style>
</head>
<body>

<section class="card card--back" aria-label="Card back">
  <div class="brand-lockup">
    <div class="brand"><span class="brand__dot"></span>Toffee Parlour</div>
    <div class="brand-rule"></div>
  </div>
  <div class="color-strip">
    <span class="blue"></span><span class="magenta"></span><span class="orange"></span>
    <span class="green"></span><span class="purple"></span><span class="black"></span>
  </div>
</section>

<section class="card card--front" aria-label="Card front">
  <div class="brand-lockup">
    <div class="brand"><span class="brand__dot"></span>Toffee Parlour</div>
    <div class="brand-rule"></div>
  </div>

  <div class="title-band">CEO &amp; Candy Stylist</div>
  <div class="name-band">Renata Hollis</div>

  <ul class="contact-list">
    <li>
      <svg viewBox="0 0 24 24" aria-hidden="true"><path fill="#1f73a8" d="M6.6 10.8a15.1 15.1 0 0 0 6.6 6.6l2.2-2.2a1 1 0 0 1 1-.25 11.4 11.4 0 0 0 3.6.57 1 1 0 0 1 1 1V20a1 1 0 0 1-1 1A17 17 0 0 1 3 4a1 1 0 0 1 1-1h3.5a1 1 0 0 1 1 1c0 1.25.2 2.45.57 3.57a1 1 0 0 1-.25 1z"/></svg>
      415.372.6091
    </li>
    <li>
      <svg viewBox="0 0 24 24" aria-hidden="true"><rect x="2" y="5" width="20" height="14" rx="1.5" fill="#1f73a8"/><path d="M3 6l9 7 9-7" fill="none" stroke="#fff" stroke-width="1.6"/></svg>
      renata@toffeeparlourco.example
    </li>
    <li>
      <svg viewBox="0 0 24 24" aria-hidden="true"><g fill="none" stroke="#1f73a8" stroke-width="1.8"><circle cx="12" cy="12" r="9"/><ellipse cx="12" cy="12" rx="4" ry="9"/><path d="M3 12h18M5 7h14M5 17h14"/></g></svg>
      www.toffeeparlourco.example
    </li>
  </ul>

  <div class="color-strip">
    <span class="blue"></span><span class="magenta"></span><span class="orange"></span>
    <span class="green"></span><span class="purple"></span><span class="black"></span>
  </div>
</section>

</body>
</html>
```